Corvane Industries business cards

We need business cards for our company Corvane Industries, based in Brisbane but trading world wide. We buy and sell Corvane Industries, generators and marine equipment. The design needs to be kept clean, simple but eye catching.
Please keep with our current logo (included) and further information can be included on request

Business

0792cd
33a6d7
85cae6
3276b5
0455a3
cedeed
cee9f5
ffffff

```html
<!DOCTYPE html>
<html lang="en">
<head>
<meta charset="utf-8">
<title>Corvane Industries business cards</title>
<link href="https://fonts.googleapis.com/css2?family=Open+Sans:wght@400;600&display=swap" rel="stylesheet">
<style>
  :root {
    --blue-deep: #0455a3;
    --blue-main: #0792cd;
    --blue-mid: #3276b5;
    --blue-light: #33a6d7;
    --blue-soft: #85cae6;
    --grey-pale: #cedeed;
    --ice: #cee9f5;
    --white: #ffffff;
    --stage: #eef1f4;
  }
  * { margin: 0; padding: 0; box-sizing: border-box; }
  html, body {
    width: 1200px; height: 818px; overflow: hidden;
    background: var(--stage);
    font-family: "Open Sans", sans-serif;
  }
  .sheet {
    width: 1200px; height: 818px;
    display: flex; align-items: center; justify-content: center; gap: 50px;
  }
  .card {
    position: relative;
    width: 525px; height: 300px;
    border-radius: 18px; overflow: hidden;
    background: linear-gradient(160deg, var(--white) 0%, var(--ice) 100%);
    box-shadow: 0 10px 28px rgba(4, 85, 163, 0.18);
  }
  .card-shape { position: absolute; inset: 0; }
  .brand {
    position: absolute; display: flex; align-items: center; gap: 14px;
    color: var(--blue-light);
  }
  .brand-mark {
    width: 46px; height: 46px; border-radius: 9px;
    background: var(--blue-light);
  }
  .brand-name { font-size: 27px; font-weight: 400; line-height: 1; letter-spacing: 0.2px; }
  .brand-suffix { display: block; font-size: 11px; margin-top: 5px; text-align: right; }
  .card--front .brand { left: 110px; top: 30px; }
  .card--back .brand { left: 50%; top: 50%; transform: translate(-50%, -50%); }
  .card--back .brand-name { font-size: 32px; }
  .card--back .brand-mark { width: 54px; height: 54px; border-radius: 11px; }

  .contact {
    position: absolute; left: 34px; top: 150px;
    color: var(--white);
  }
  .contact-name { font-size: 20px; font-weight: 600; line-height: 1.1; }
  .contact-role { font-size: 12px; margin-top: 2px; }
  .contact-address { font-size: 11.5px; line-height: 1.35; margin-top: 12px; }
  .contact-lines { list-style: none; margin-top: 10px; font-size: 11.5px; line-height: 1.45; }
  .contact-lines li { display: flex; align-items: center; gap: 8px; }
  .contact-lines svg { width: 11px; height: 11px; flex: none; }
</style>
</head>
<body>
<main class="sheet">
  <section class="card card--front" aria-label="Business card front">
    <svg class="card-shape" viewBox="0 0 525 300" preserveAspectRatio="none" aria-hidden="true">
      <defs>
        <linearGradient id="band" x1="0" y1="0" x2="1" y2="1">
          <stop offset="0" stop-color="#0792cd"/>
          <stop offset="1" stop-color="#0455a3"/>
        </linearGradient>
      </defs>
      <path d="M0,112 C170,150 360,150 525,96 L525,300 L0,300 Z" fill="url(#band)"/>
      <path d="M0,104 C170,142 360,142 525,88" fill="none" stroke="#33a6d7" stroke-width="2"/>
    </svg>
    <div class="brand">
      <span class="brand-mark"></span>
      <span class="brand-name">Corvane Industries<span class="brand-suffix">Pty Ltd</span></span>
    </div>
    <div class="contact">
      <p class="contact-name">Employee Name</p>
      <p class="contact-role">Managing Director</p>
      <p class="contact-address">Your Adress Inc 2nd Lane<br>Ave Marlton, QL 00000</p>
      <ul class="contact-lines">
        <li><svg viewBox="0 0 12 12"><circle cx="6" cy="3.5" r="2.6" fill="#fff"/><path d="M1 12 C1 7 11 7 11 12 Z" fill="#fff"/></svg>0012 3456 789</li>
        <li><svg viewBox="0 0 12 12"><rect x="0.5" y="2" width="11" height="8" fill="#fff"/><path d="M0.5 2 L6 7 L11.5 2" fill="none" stroke="#0455a3" stroke-width="1"/></svg>info@youremail.com</li>
        <li><svg viewBox="0 0 12 12"><circle cx="6" cy="6" r="5.5" fill="#fff"/><path d="M0.5 6 H11.5 M6 0.5 C3 3 3 9 6 11.5 M6 0.5 C9 3 9 9 6 11.5" fill="none" stroke="#0455a3" stroke-width="0.8"/></svg>www.yourwebsite.com</li>
      </ul>
    </div>
  </section>

  <section class="card card--back" aria-label="Business card back">
    <div class="brand">
      <span class="brand-mark"></span>
      <span class="brand-name">Corvane Industries<span class="brand-suffix">Pty Ltd</span></span>
    </div>
  </section>
</main>
</body>
</html>
```